Corliss Homes Website for luxury custom home builder with endless detail

Modern website for luxury custom home builder. Simple and easy for viewers to understand what we do. New company formed by retired custom home builder. Company concept is to simplify the building experience with modern technology and introduce a simple pricing strategy for the client. Website must flow. Prefer page less design or possibly something that is up and coming within the web design community. Two galleries: INTERIOR and EXTERIOR. I would like two click on box's when the website is opened showing the galleries as a centerpiece and would also prefer them to play as a slide show. The page needs to fit the entire screen in size. We would like to use Grey, Black and White or the shade of blue that is in our company logo. I would like to see one of my uploaded photos to be in the background. I would also like a 3rd box that will play some type of animated video describing what we do and what our process is. Hoping this would be more interactive for the viewer than clicking on buttons and navigating around wasting time.

Target Market(s)

affluent buyers ages 30-60 who want to built anything from large estates to downsized luzury homes for the retired crowd.

Industry/Entity Type

Home Builder

Number of Pages Required

1 page

Font styles to use
Sans Serif

Colors
33a6d7
000000
333333
5c5c5c
9d9d9d
d9d9d9

Requirements
Must have
• Logo and name at top of page. I would like a pageless web design that includes two gallery box's (Interior and Exterior photos) side by side on the first page. I would also like a 3rd box that will be a eVideo explaining what we do and how we do it. I want as little text as possible. I would like the background to be of one of my interior photos that will flow best and pop when the page loads.

```html
<!DOCTYPE html>
<html lang="en">
<head>
<meta charset="utf-8">
<title>Corliss Homes</title>
<link href="https://fonts.googleapis.com/css2?family=Cinzel:wght@400;700&family=Open+Sans:wght@400;600&display=swap" rel="stylesheet">
<style>
:root{
  --blue:#33a6d7;
  --black:#000000;
  --charcoal:#333333;
  --slate:#5c5c5c;
  --grey:#9d9d9d;
  --mist:#d9d9d9;
  --paper:#ffffff;
  --panel:#ececec;
  --footer:#2b2b2b;
}
*{box-sizing:border-box;margin:0;padding:0}
html,body{width:804px;height:1200px;overflow:hidden}
body{font-family:"Open Sans",Arial,sans-serif;color:var(--slate);background:var(--paper)}
.serif{font-family:"Cinzel",Georgia,serif}

/* hero */
.hero{position:relative;height:420px;overflow:hidden}
.hero-photo{position:absolute;inset:0;background:
  radial-gradient(ellipse at 70% 20%,rgba(210,200,185,.55),transparent 55%),
  linear-gradient(160deg,#6b6157 0%,#4d443c 35%,#3a332d 60%,#6e665c 100%)}
.hero-shade{position:absolute;inset:0;background:rgba(0,0,0,.28)}
.topbar{position:absolute;top:0;left:0;right:0;height:46px;background:rgba(0,0,0,.75);display:flex;align-items:center;justify-content:space-between;padding:0 16px 0 14px}
.brand{display:flex;flex-direction:column;align-items:center;margin-top:14px}
.brand-mark{width:34px;height:34px;border:1px solid var(--grey);background:#1d3240}
.brand-name{font-family:"Cinzel",Georgia,serif;font-size:9px;color:var(--paper);letter-spacing:1px;margin-top:3px;white-space:nowrap}
.nav{display:flex;gap:18px;list-style:none}
.nav li{font-family:"Cinzel",Georgia,serif;font-size:9px;color:var(--paper);display:flex;align-items:center;gap:6px}
.nav li::before{content:"";width:4px;height:4px;background:var(--paper)}
.nav li.active{color:var(--blue)}
.nav li.active::before{background:var(--blue)}
.hero-copy{position:absolute;top:176px;left:0;right:0;text-align:center;color:var(--paper)}
.hero-title{font-size:40px;letter-spacing:6px;font-weight:400}
.hero-sub{font-size:14px;letter-spacing:3px;margin-top:4px}
.btn{display:inline-block;background:var(--blue);color:var(--paper);font-size:8px;font-weight:600;letter-spacing:1px;padding:7px 14px}
.hero-copy .btn{margin-top:16px}
.arrow{position:absolute;top:196px;width:14px;height:24px}
.arrow.left{left:10px}.arrow.right{right:10px}
.dots{display:flex;gap:4px;justify-content:center}
.dots span{width:7px;height:7px;border-radius:50%;border:1px solid var(--grey);background:transparent}
.dots span.on{background:var(--mist)}
.hero .dots{position:absolute;bottom:26px;left:0;right:0}

/* welcome */
.welcome{height:115px;text-align:center;padding-top:26px}
.section-title{font-size:17px;letter-spacing:2px;color:var(--charcoal);font-weight:400}
.welcome p{font-size:7.5px;line-height:1.6;color:var(--grey);width:470px;margin:10px auto 0}

/* gallery */
.gallery{height:290px;background:var(--panel);text-align:center;padding-top:26px}
.tabs{display:flex;justify-content:center;gap:10px;margin-top:8px;font-size:7.5px;letter-spacing:1px}
.tabs span{display:flex;align-items:center;gap:5px;color:var(--blue)}
.tabs span::before{content:"";width:4px;height:4px;background:var(--blue)}
.tabs span.muted{color:var(--slate)}
.tabs span.muted::before{background:var(--slate)}
.grid{display:grid;grid-template-columns:repeat(4,165px);gap:5px;justify-content:center;margin-top:12px}
.tile{height:85px}
.t1{background:linear-gradient(135deg,#5a4230,#a3876a)}
.t2{background:linear-gradient(135deg,#3b2b20,#8c6a4a)}
.t3{background:linear-gradient(135deg,#6d5a48,#c2a888)}
.t4{background:linear-gradient(135deg,#7a5630,#d8a968)}
.t5{background:linear-gradient(135deg,#4a3526,#b08858)}
.t6{background:linear-gradient(135deg,#5c4632,#9b7c5c)}
.t7{background:linear-gradient(135deg,#6a4a2a,#c79a5c)}
.t8{background:linear-gradient(135deg,#3e3026,#8a6e52)}
.gallery .dots{margin-top:12px}

/* what we do */
.about{height:310px;display:flex;justify-content:space-between;padding:40px 64px 0 65px}
.about-copy{width:330px}
.about-copy .section-title{text-align:left}
.about-copy p{font-size:7.5px;line-height:1.7;color:var(--grey);margin:16px 0 20px}
.video{position:relative;width:300px;height:182px;margin-top:64px;background:linear-gradient(180deg,#8fb0c8 0%,#b9c6cf 45%,#5d6a4a 75%,#3b4630 100%)}
.video-side{position:absolute;top:8px;right:8px;display:flex;flex-direction:column;gap:4px}
.video-side span{width:16px;height:14px;background:rgba(0,0,0,.7)}
.video-play{position:absolute;left:50%;top:50%;width:44px;height:30px;margin:-15px 0 0 -22px;background:rgba(0,0,0,.75);border-radius:4px}
.video-bar{position:absolute;left:0;right:0;bottom:0;height:16px;background:rgba(0,0,0,.75);display:flex;align-items:center;padding:0 6px;gap:6px}
.video-bar .track{flex:1;height:3px;background:var(--slate)}
.video-bar .time{font-size:6px;color:var(--paper)}

/* footer */
.footer{position:absolute;left:0;right:0;bottom:0;height:55px;background:var(--footer);display:flex;align-items:center;justify-content:space-between;padding:0 24px}
.footer small{font-size:6.5px;color:var(--grey)}
.social{display:flex;gap:5px}
.social span{width:11px;height:11px;background:var(--mist)}
</style>
</head>
<body>

<section class="hero">
  <div class="hero-photo" role="img" aria-label="Photo of a luxury home interior with a wicker armchair, large window and a staircase"></div>
  <div class="hero-shade"></div>
  <header class="topbar">
    <div class="brand">
      <span class="brand-mark"></span>
      <span class="brand-name">Corliss Homes</span>
    </div>
    <ul class="nav">
      <li class="active">Home</li>
      <li>About Us</li>
      <li>Services</li>
      <li>Projects</li>
      <li>Gallery</li>
      <li>Contact Us</li>
    </ul>
  </header>
  <svg class="arrow left" viewBox="0 0 14 24"><path d="M11 2 2 12l9 10" fill="none" stroke="#fff" stroke-width="2"/></svg>
  <svg class="arrow right" viewBox="0 0 14 24"><path d="M3 2l9 10-9 10" fill="none" stroke="#fff" stroke-width="2"/></svg>
  <div class="hero-copy">
    <h1 class="hero-title serif">Corliss Homes</h1>
    <p class="hero-sub serif">WE ARE LUXURY CUSTOM HOME BUILDER</p>
    <span class="btn">LEARN MORE</span>
  </div>
  <div class="dots"><span class="on"></span><span></span><span></span></div>
</section>

<section class="welcome">
  <h2 class="section-title serif">WELCOME TO CORLISS HOMES</h2>
  <p>We design and build custom homes with care for every detail, from the first sketch to the final walkthrough. Our process keeps each step clear, simple and fairly priced for every client we serve.</p>
</section>

<section class="gallery">
  <h2 class="section-title serif">OUR GALLERY</h2>
  <div class="tabs"><span>INTERIOR</span><span class="muted">EXTERIOR</span></div>
  <div class="grid">
    <div class="tile t1" role="img" aria-label="Interior photo of a dining room"></div>
    <div class="tile t2" role="img" aria-label="Interior photo of a living room"></div>
    <div class="tile t3" role="img" aria-label="Interior photo of a kitchen"></div>
    <div class="tile t4" role="img" aria-label="Interior photo of a wood kitchen"></div>
    <div class="tile t5" role="img" aria-label="Interior photo of a great room"></div>
    <div class="tile t6" role="img" aria-label="Interior photo of a fireplace"></div>
    <div class="tile t7" role="img" aria-label="Interior photo of a kitchen island"></div>
    <div class="tile t8" role="img" aria-label="Interior photo of a family room"></div>
  </div>
  <div class="dots"><span class="on"></span><span></span><span></span></div>
</section>

<section class="about">
  <div class="about-copy">
    <h2 class="section-title serif">WHAT WE DO</h2>
    <p>We guide you through planning, design and construction with one team and one clear price. Modern tools let you follow progress from anywhere, so decisions stay simple and timelines stay on track. Whether you want a grand estate or a smaller retreat, every home is built to last and finished with the details that make it yours.</p>
    <span class="btn">LEARN MORE</span>
  </div>
  <div class="video" role="img" aria-label="Video still of a large custom timber home exterior under a blue sky">
    <div class="video-side"><span></span><span></span><span></span></div>
    <div class="video-play">
      <svg width="44" height="30" viewBox="0 0 44 30"><path d="M18 9v12l10-6z" fill="#fff"/></svg>
    </div>
    <div class="video-bar">
      <svg width="8" height="8" viewBox="0 0 8 8"><path d="M1 0v8l7-4z" fill="#fff"/></svg>
      <span class="track"></span>
      <span class="time">00:00</span>
    </div>
  </div>
</section>

<footer class="footer">
  <small>Copyright © 2015, Corliss Homes - All Rights Reserved</small>
  <div class="social"><span></span><span></span><span></span><span></span><span></span></div>
</footer>

</body>
</html>
```